Livestock Consulting Company has a logo but needs business cards and a uniform logo

My company works with farmers advising them on managing cattle and sheep. I have a logo but need business cards and a version of my logo to go onto my work shirts. I need the following wording added to my logo for my shirts "Tallowby Livestock Consulting".

```html
<!DOCTYPE html>
<html lang="en">
<head>
<meta charset="utf-8">
<title>Tallowby Livestock Consulting – Business Cards</title>
<link href="https://fonts.googleapis.com/css2?family=Nunito+Sans:wght@700&family=Arimo:wght@400;700&display=swap" rel="stylesheet">
<style>
  :root {
    --backdrop: #2b2b2b;
    --brown-deep: #553e28;
    --brown-mid: #6f5a45;
    --brown-logo: #8a7560;
    --brown-text: #5a4530;
    --paper: #ffffff;
    --ink-light: #ffffff;
    --shadow: rgba(0,0,0,0.5);
  }
  * { margin: 0; padding: 0; box-sizing: border-box; }
  html, body { width: 1200px; height: 900px; overflow: hidden; }
  body {
    background: var(--backdrop);
    position: relative;
    font-family: "Arimo", Arial, sans-serif;
  }
  .card {
    position: absolute;
    left: 250px;
    width: 700px;
    height: 400px;
    box-shadow: 0 12px 30px var(--shadow);
    overflow: hidden;
  }
  /* Front */
  .card-front {
    top: 35px;
    background: linear-gradient(180deg, #5e4630 0%, var(--brown-deep) 100%);
    display: flex;
    align-items: center;
    justify-content: center;
  }
  .wordmark {
    display: flex;
    align-items: center;
    gap: 14px;
    font-family: "Nunito Sans", sans-serif;
    font-weight: 700;
    font-size: 30px;
    letter-spacing: 1px;
    text-transform: uppercase;
    line-height: 1.15;
  }
  .wordmark-dot {
    width: 16px; height: 16px; border-radius: 50%;
    flex: none;
  }
  .card-front .wordmark { color: var(--ink-light); }
  .card-front .wordmark-dot { background: var(--ink-light); }

  /* Back */
  .card-back {
    top: 465px;
    background: var(--paper);
  }
  .card-back .wordmark {
    position: absolute;
    right: 40px;
    top: 55px;
    font-size: 24px;
    color: var(--brown-text);
    text-align: right;
  }
  .card-back .wordmark-dot { background: var(--brown-text); }
  .band {
    position: absolute;
    left: 0; top: 232px;
    width: 700px; height: 128px;
    background: var(--brown-deep);
  }
  .band-accent {
    position: absolute;
    left: 0; top: 150px;
    width: 700px; height: 210px;
  }
  .trim-stripe {
    position: absolute;
    left: 0; top: 378px;
    width: 700px; height: 8px;
    background: var(--brown-deep);
  }
  .person {
    position: absolute;
    right: 40px; top: 170px;
    text-align: right;
    color: var(--ink-light);
  }
  .person-name { font-weight: 700; font-size: 26px; }
  .person-role { font-size: 15px; margin-top: 2px; }
  .address {
    position: absolute;
    right: 40px; top: 262px;
    text-align: right;
    color: var(--ink-light);
    font-size: 17px;
    line-height: 1.45;
  }
  .address-line { display: flex; align-items: center; justify-content: flex-end; gap: 8px; }
  .contacts {
    position: absolute;
    left: 40px; top: 246px;
    list-style: none;
    color: var(--ink-light);
    font-size: 18px;
  }
  .contacts li {
    display: flex; align-items: center; gap: 16px;
    height: 26px;
  }
  .contacts svg { width: 16px; height: 16px; flex: none; }
</style>
</head>
<body>

<section class="card card-front" aria-label="Business card front">
  <div class="wordmark">
    <span class="wordmark-dot"></span>
    <span>Tallowby Livestock<br>Consulting</span>
  </div>
</section>

<section class="card card-back" aria-label="Business card back">
  <svg class="band-accent" viewBox="0 0 700 210" aria-hidden="true">
    <path d="M450 0 H700 V210 H420 V82 L395 110 L440 70 V20 Q440 0 460 0 Z" fill="var(--brown-mid)"/>
  </svg>
  <div class="band" style="width:420px"></div>

  <div class="wordmark">
    <span class="wordmark-dot"></span>
    <span>Tallowby Livestock<br>Consulting</span>
  </div>

  <div class="person">
    <div class="person-name">Marlo Pennick</div>
    <div class="person-role">Manager</div>
  </div>

  <div class="address">
    <div class="address-line">14 Crestfield Ln,
      <svg width="14" height="14" viewBox="0 0 16 16" aria-hidden="true"><path d="M8 1 L15 8 H13 V15 H3 V8 H1 Z" fill="#fff"/></svg>
    </div>
    <div>Alder Vale OR 97321, Suite 210</div>
  </div>

  <ul class="contacts">
    <li>
      <svg viewBox="0 0 16 16" aria-hidden="true"><path d="M3 1 L6 1 L7 5 L5 6.5 Q6.5 9.5 9.5 11 L11 9 L15 10 V13 Q15 15 13 15 Q2 14 1 3 Q1 1 3 1 Z" fill="#fff"/></svg>
      <span>012 3456 7890</span>
    </li>
    <li>
      <svg viewBox="0 0 16 16" aria-hidden="true"><rect x="4" y="1" width="8" height="14" rx="1.5" fill="none" stroke="#fff" stroke-width="1.5"/><circle cx="8" cy="12.5" r="0.9" fill="#fff"/></svg>
      <span>012 3456 7890</span>
    </li>
    <li>
      <svg viewBox="0 0 16 16" aria-hidden="true"><rect x="1" y="3" width="14" height="10" fill="#fff"/><path d="M1 3 L8 9 L15 3" fill="none" stroke="var(--brown-deep)" stroke-width="1.2"/></svg>
      <span>info@yourwebsite.com</span>
    </li>
    <li>
      <svg viewBox="0 0 16 16" aria-hidden="true"><circle cx="8" cy="8" r="6.5" fill="none" stroke="#fff" stroke-width="1.3"/><ellipse cx="8" cy="8" rx="3" ry="6.5" fill="none" stroke="#fff" stroke-width="1"/><path d="M1.5 8 H14.5 M2.5 5 H13.5 M2.5 11 H13.5" stroke="#fff" stroke-width="1"/></svg>
      <span>www.yourwebsite.com</span>
    </li>
  </ul>

  <div class="trim-stripe"></div>
</section>

</body>
</html>
```